Flyer for the Harvest Lantern Gathering 2018

Design a flyer for our annual conference with basic information about the conference: conference logo and year,

Location:
Dunmore Community Center (Downtown Portland)
482 Willowby Street, Portland, ME 04117,

Date:
August 24th, 25th and 26th, 2018
Start time 6:00PM

I would like the following three words added to the flyer. These words describe the vision of the conference:
Prophetic, Worship, Prayer

```html
<!DOCTYPE html>
<html lang="en">
<head>
<meta charset="utf-8">
<title>Harvest Lantern Gathering 2018</title>
<link rel="stylesheet" href="https://fonts.googleapis.com/css2?family=Oswald:wght@400;500;600;700&family=Roboto+Condensed:wght@400;700&display=swap">
<style>
  :root {
    --orange: #f07a1c;
    --orange-deep: #e0610f;
    --orange-light: #f89a3a;
    --charcoal: #3a3a3c;
    --ink: #2f2f31;
    --white: #ffffff;
    --sky-top: #8a4a22;
    --sky-mid: #e8872e;
    --sky-glow: #f8c978;
    --hill: #1c1410;
  }
  * { margin: 0; padding: 0; box-sizing: border-box; }
  html, body { width: 849px; height: 1200px; overflow: hidden; background: var(--white); }
  .flyer {
    position: relative;
    width: 849px;
    height: 1200px;
    overflow: hidden;
    background: var(--white);
    font-family: "Roboto Condensed", "Arial Narrow", sans-serif;
  }
  .hero {
    position: absolute;
    inset: 0 0 auto 0;
    height: 700px;
    background:
      radial-gradient(ellipse 420px 260px at 78% 38%, var(--sky-glow) 0%, rgba(248,201,120,0) 70%),
      linear-gradient(180deg, var(--sky-top) 0%, var(--sky-mid) 40%, #b8561e 58%, var(--hill) 72%, var(--hill) 100%);
  }
  .shapes { position: absolute; inset: 0; }
  .brand {
    position: absolute;
    top: 48px;
    left: 48px;
    display: flex;
    align-items: center;
    gap: 16px;
  }
  .brand-mark {
    width: 62px;
    height: 62px;
    border-radius: 50%;
    background: var(--orange);
  }
  .brand-name {
    font-family: "Oswald", sans-serif;
    font-weight: 500;
    font-size: 38px;
    letter-spacing: 2px;
    color: var(--white);
  }
  .vision {
    position: absolute;
    top: 128px;
    left: 48px;
    font-family: "Oswald", sans-serif;
    font-weight: 500;
    font-size: 20px;
    letter-spacing: 3px;
    text-transform: uppercase;
    color: var(--white);
  }
  .title-block {
    position: absolute;
    left: 0;
    width: 849px;
    top: 612px;
    text-align: center;
    transform: rotate(-8.4deg);
    color: var(--white);
    font-family: "Oswald", sans-serif;
    white-space: nowrap;
  }
  .event-name {
    font-weight: 700;
    font-size: 60px;
    line-height: 1.05;
    text-transform: uppercase;
    letter-spacing: 0.5px;
  }
  .event-year {
    margin-top: 2px;
    font-weight: 500;
    font-size: 44px;
    line-height: 1.1;
  }
  .details {
    position: absolute;
    top: 835px;
    left: 0;
    width: 849px;
    text-align: center;
    color: var(--ink);
  }
  .detail-label {
    font-family: "Oswald", sans-serif;
    font-weight: 500;
    font-size: 38px;
    line-height: 1.1;
    color: var(--orange);
  }
  .detail-line {
    font-weight: 700;
    font-size: 25px;
    line-height: 1.25;
  }
  .detail-group + .detail-group { margin-top: 28px; }
  .contact {
    position: absolute;
    left: 0;
    bottom: 0;
    width: 849px;
    height: 120px;
    background: var(--orange);
    border-top: 8px solid var(--charcoal);
    color: var(--white);
    text-align: center;
  }
  .contact-title {
    margin-top: 12px;
    font-family: "Oswald", sans-serif;
    font-weight: 500;
    font-size: 27px;
  }
  .contact-list {
    list-style: none;
    margin-top: 12px;
    display: flex;
    justify-content: center;
    gap: 70px;
    font-size: 22px;
  }
  .contact-item { display: flex; align-items: center; gap: 10px; }
  .contact-item svg { width: 22px; height: 22px; }
</style>
</head>
<body>
<main class="flyer">
  <div class="hero" role="img" aria-label="Photo of a sunset sky glowing orange above a dark silhouetted hill crowned with a cross"></div>

  <svg class="shapes" width="849" height="1200" viewBox="0 0 849 1200" aria-hidden="true">
    <polygon points="0,600 849,470 849,1200 0,1200" fill="var(--white)"/>
    <polygon points="0,640 849,515 849,725 0,830" fill="var(--orange)"/>
    <polygon points="0,640 849,515 849,560 0,680" fill="var(--orange-light)" opacity="0.55"/>
    <polygon points="620,750 849,722 849,745 640,770" fill="var(--charcoal)"/>
  </svg>

  <header class="brand">
    <span class="brand-mark"></span>
    <span class="brand-name">LANTERNCON</span>
  </header>
  <p class="vision">Prophetic · Worship · Prayer</p>

  <section class="title-block">
    <h1 class="event-name">Harvest Lantern Gathering</h1>
    <p class="event-year">2018</p>
  </section>

  <section class="details">
    <div class="detail-group">
      <h2 class="detail-label">Location:</h2>
      <p class="detail-line">Dunmore Community Center (Downtown Portland)</p>
      <p class="detail-line">482 Willowby Street, Portland, ME 04117,</p>
    </div>
    <div class="detail-group">
      <h2 class="detail-label">Date:</h2>
      <p class="detail-line">August 24th, 25th and 26th, 2018</p>
      <p class="detail-line">Start time 6:00PM</p>
    </div>
  </section>

  <footer class="contact">
    <h3 class="contact-title">Contact</h3>
    <ul class="contact-list">
      <li class="contact-item">
        <svg viewBox="0 0 24 24"><path fill="currentColor" d="M6.6 10.8a15.1 15.1 0 0 0 6.6 6.6l2.2-2.2a1 1 0 0 1 1-.25 11.4 11.4 0 0 0 3.6.57 1 1 0 0 1 1 1V20a1 1 0 0 1-1 1A17 17 0 0 1 3 4a1 1 0 0 1 1-1h3.5a1 1 0 0 1 1 1c0 1.25.2 2.45.57 3.57a1 1 0 0 1-.25 1z"/></svg>
        (555) 014 2290
      </li>
      <li class="contact-item">
        <svg viewBox="0 0 24 24"><rect x="3" y="5.5" width="18" height="13" fill="none" stroke="currentColor" stroke-width="2"/><polyline points="3.5,6.5 12,13 20.5,6.5" fill="none" stroke="currentColor" stroke-width="2"/></svg>
        hello@lanternmail.org
      </li>
      <li class="contact-item">
        <svg viewBox="0 0 24 24" fill="none" stroke="currentColor" stroke-width="1.8"><circle cx="12" cy="12" r="9"/><ellipse cx="12" cy="12" rx="4" ry="9"/><line x1="3" y1="12" x2="21" y2="12"/></svg>
        website
      </li>
    </ul>
  </footer>
</main>
</body>
</html>
```